Meridian Lodging Partners

An Editable Business Card Template For MLP & MLH
Similar or Different Design

418 W. Harlan Brookside Pkwy.
Suite 2270
Irving, TX 75091

```html
<!DOCTYPE html>
<html lang="en">
<head>
<meta charset="utf-8">
<title>Meridian Lodging Partners – Business Cards</title>
<link href="https://fonts.googleapis.com/css2?family=Inter:wght@400;600;700;800&display=swap" rel="stylesheet">
<style>
  :root {
    --backdrop: #8e8e8e;
    --card: #ffffff;
    --brand-red: #921b20;
    --accent-red: #a61e24;
    --ink: #141414;
    --text-grey: #4a4a4a;
  }
  * { box-sizing: border-box; margin: 0; padding: 0; }
  html, body { width: 1200px; height: 1200px; overflow: hidden; }
  body {
    background: var(--backdrop);
    font-family: "Inter", Arial, sans-serif;
    position: relative;
  }
  .card {
    position: absolute;
    left: 269px;
    width: 663px;
    height: 380px;
    background: var(--card);
    box-shadow: 2px 3px 6px rgba(0,0,0,0.3);
    overflow: hidden;
  }
  .card--front { top: 180px; }
  .card--back { top: 630px; }
  .brand-band {
    position: absolute; left: 0; top: 0;
    width: 152px; height: 100%;
    background: var(--brand-red);
  }
  .brand-mark {
    position: absolute;
    left: 34px; top: 86px;
    width: 208px; height: 208px;
    border-radius: 50%;
    background: var(--card);
    display: flex; flex-direction: column;
    align-items: center; justify-content: center;
    color: var(--brand-red);
    font-weight: 700;
    text-align: center;
  }
  .brand-mark__initials { font-size: 46px; line-height: 1; letter-spacing: 1px; }
  .brand-mark__name { font-size: 14px; line-height: 1.35; margin-top: 12px; }

  .contact { position: absolute; left: 359px; top: 76px; }
  .contact__name { font-size: 26px; font-weight: 700; color: var(--ink); letter-spacing: 0.5px; line-height: 1.1; }
  .contact__role { font-size: 16px; color: var(--accent-red); margin-top: 1px; }
  .contact__address { font-size: 15px; color: var(--text-grey); line-height: 20px; margin-top: 12px; letter-spacing: 0.3px; }
  .contact__lines { margin-top: 10px; list-style: none; }
  .contact__lines li { display: flex; align-items: center; color: var(--text-grey); letter-spacing: 0.3px; }
  .contact__lines .phone { font-size: 20px; height: 24px; }
  .contact__lines .small { font-size: 15px; height: 18px; }
  .contact__lines svg { width: 12px; height: 12px; margin-right: 9px; flex: none; }
  .highlight { color: var(--accent-red); }

  .pitch { position: absolute; left: 359px; top: 76px; width: 280px; }
  .pitch__headline {
    font-size: 19px; font-weight: 800; color: var(--brand-red);
    line-height: 21px; letter-spacing: 0.4px;
  }
  .pitch__list { list-style: none; margin-top: 12px; }
  .pitch__list li {
    position: relative; padding-left: 26px;
    font-size: 14px; color: var(--text-grey); line-height: 16px;
    margin-bottom: 6px; letter-spacing: 0.2px;
  }
  .pitch__list svg { position: absolute; left: 0; top: 3px; width: 18px; height: 10px; }
</style>
</head>
<body>

<section class="card card--front">
  <div class="brand-band"></div>
  <div class="brand-mark">
    <span class="brand-mark__initials">MLH</span>
    <span class="brand-mark__name">Meridian<br>Lodging<br>Housing</span>
  </div>
  <div class="contact">
    <h1 class="contact__name">DANA WHITFIELD</h1>
    <p class="contact__role">Sales Manager</p>
    <p class="contact__address">418 W. Harlan Brookside Pkwy.<br>Suite 2270<br>Irving, TX 75091</p>
    <ul class="contact__lines">
      <li class="phone"><svg viewBox="0 0 12 12"><path fill="#a61e24" d="M2.4 1l2 2.1-1 1.2c.6 1.4 1.6 2.4 3 3l1.2-1L9.8 8.4 8.6 10.6C5 10.2 1.8 7 1.4 3.4z"/></svg>214-555-0148</li>
      <li class="phone"><svg viewBox="0 0 12 12"><rect x="3" y="0.5" width="6" height="11" rx="1.2" fill="none" stroke="#a61e24" stroke-width="1.4"/><circle cx="6" cy="9.2" r="0.8" fill="#a61e24"/></svg>480-555-0173</li>
      <li class="small"><svg viewBox="0 0 12 12"><rect x="0.5" y="2.5" width="11" height="7.5" fill="#a61e24"/><path d="M0.8 2.8L6 7l5.2-4.2" fill="none" stroke="#fff" stroke-width="1"/></svg>DWhitfield@meridianlodging.com</li>
      <li class="small"><svg viewBox="0 0 12 12"><circle cx="6" cy="6" r="5.5" fill="#a61e24"/><path d="M3 3.5c1.5 0 2 1 1.6 2.2C4.2 7 5 8.5 6 9M7 2.5c.5 1 1.8 1.5 2.5 1.3M7.5 6.5c1 0 1.5.8 1.2 1.8" stroke="#fff" stroke-width="1" fill="none"/></svg>www.<span class="highlight">MLPOilField</span>.com</li>
    </ul>
  </div>
</section>

<section class="card card--back">
  <div class="brand-band"></div>
  <div class="brand-mark">
    <span class="brand-mark__initials">MLP</span>
    <span class="brand-mark__name">Meridian<br>Lodging<br>Partners</span>
  </div>
  <div class="pitch">
    <h2 class="pitch__headline">EXPERIENCED<br>PROVIDER TO OIL,<br>GAS, ENERGY &amp;<br>CONSTRUCTION<br>INDUSTRIES</h2>
    <ul class="pitch__list">
      <li><svg viewBox="0 0 18 10"><path d="M1 9L16 2M11 1.5h5.5V6" fill="none" stroke="#a61e24" stroke-width="1.8"/></svg>Consolidated Billing</li>
      <li><svg viewBox="0 0 18 10"><path d="M1 9L16 2M11 1.5h5.5V6" fill="none" stroke="#a61e24" stroke-width="1.8"/></svg>Full Service Corporate Lodging</li>
      <li><svg viewBox="0 0 18 10"><path d="M1 9L16 2M11 1.5h5.5V6" fill="none" stroke="#a61e24" stroke-width="1.8"/></svg>Live Customer Support 24/7/365</li>
      <li><svg viewBox="0 0 18 10"><path d="M1 9L16 2M11 1.5h5.5V6" fill="none" stroke="#a61e24" stroke-width="1.8"/></svg>Proven Track Record Of Performance</li>
      <li><svg viewBox="0 0 18 10"><path d="M1 9L16 2M11 1.5h5.5V6" fill="none" stroke="#a61e24" stroke-width="1.8"/></svg>Best Negotiated Rates &amp;<br>No Additional Fees</li>
    </ul>
  </div>
</section>

</body>
</html>
```